A Bold and Enticing Book Cover is needed for my new book Bright Harbor!

I need a Book Cover Design for my paperback book that will be published next Spring... The book is called:

Bright Harbor
A Pocket Map for Turning Points and Endings

I want the design to be bold and eye-catching, and not too soft or touchy feely! I'd like the fonts to be funky, and clear. I feel that the design should capture the idea of moving forwards and growth. I am a Solution Focused Hypnotherapist, and our model of therapy is direct, but also supports change in a step by step solution focused way!

I'm uploading an idea, but am so open to suggestions.

I really like the design of the BRIGHT HARBOR lettering I have used...

Looking forward to seeing your suggestions!

Thanks,

Renka :)

Target Market(s)

Readers and Browsers who are grieving or going through change...

Industry/Entity Type

Hypnotherapy

Font styles to use
Sans Serif
Other font styles liked:
• star avenue?

Requirements
Must have
• Be Bold, and Eyecatching... Maybe reference to the Brain, as I'm a hypnotherapist.
Nice to have
• Bright Colour... My website is bold, look at that www.themarlowenstudio.example but please don't just copy images off the website... I want it to have a 'feel' of the website, but not be a replica!
Should not have
• I'm not into fluffy or pastel images...

```html
<!DOCTYPE html>
<html lang="en">
<head>
<meta charset="utf-8">
<title>Bright Harbor — Book Cover</title>
<link rel="stylesheet" href="https://fonts.googleapis.com/css2?family=Jost:wght@300;600;700&display=swap">
<style>
  :root {
    --teal-top: #3a949d;
    --teal-mid: #2f8790;
    --teal-band: #2a7d87;
    --white: #ffffff;
    --tunnel-glow: #f7fbfc;
    --tunnel-light: #d9e8eb;
    --tunnel-mid: #8fb4ba;
    --tunnel-deep: #3f7d86;
    --tunnel-core: #2c666e;
  }
  html, body {
    margin: 0;
    padding: 0;
    width: 800px;
    height: 1200px;
    overflow: hidden;
    background: var(--teal-mid);
  }
  .cover {
    position: relative;
    width: 800px;
    height: 1200px;
    overflow: hidden;
    background: linear-gradient(180deg, var(--teal-top) 0%, var(--teal-mid) 35%);
    font-family: "Jost", "Helvetica Neue", Arial, sans-serif;
    color: var(--white);
  }
  .title-block {
    position: absolute;
    top: 0;
    left: 0;
    width: 800px;
    height: 421px;
    text-align: center;
  }
  .title-main {
    position: absolute;
    top: 14px;
    left: 0;
    width: 100%;
    margin: 0;
    font-weight: 700;
    font-size: 150px;
    line-height: 1;
    letter-spacing: 0.01em;
  }
  .title-sub {
    position: absolute;
    top: 176px;
    left: 0;
    width: 100%;
    margin: 0;
    font-weight: 300;
    font-size: 118px;
    line-height: 1;
    letter-spacing: 0.14em;
    padding-left: 0.14em;
    box-sizing: border-box;
  }
  .subtitle {
    position: absolute;
    top: 338px;
    left: 0;
    width: 100%;
    margin: 0;
    font-weight: 600;
    font-size: 25px;
    line-height: 1.2;
  }
  .cover-art {
    position: absolute;
    top: 421px;
    left: 0;
    width: 800px;
    height: 680px;
    background:
      radial-gradient(ellipse 16% 14% at 44% 52%, var(--tunnel-core) 0%, var(--tunnel-deep) 40%, transparent 100%),
      radial-gradient(ellipse 62% 58% at 46% 50%,
        var(--tunnel-mid) 0%,
        var(--tunnel-glow) 38%,
        var(--tunnel-light) 55%,
        var(--tunnel-mid) 75%,
        var(--tunnel-deep) 100%);
  }
  .author-band {
    position: absolute;
    left: 0;
    bottom: 0;
    width: 800px;
    height: 99px;
    background: var(--teal-band);
    display: flex;
    align-items: center;
    justify-content: center;
  }
  .author-name {
    margin: 0;
    font-weight: 700;
    font-size: 54px;
    letter-spacing: 0.02em;
    line-height: 1;
  }
</style>
</head>
<body>
  <main class="cover">
    <header class="title-block">
      <h1 class="title-main">BRIGHT</h1>
      <p class="title-sub">HARBOR</p>
      <p class="subtitle">A Pocket Map for Turning Points and Endings</p>
    </header>
    <div class="cover-art" role="img" aria-label="Photograph of a bright white spiralling tunnel of concentric rings, with a small figure striding forward towards its deep teal centre"></div>
    <footer class="author-band">
      <p class="author-name">RENKA VOSS</p>
    </footer>
  </main>
</body>
</html>
```